Wix Landing Page for Cutting-Edge Healthcare Concussion Supplement

Wix Website Design Brief: Veltoria+ Landing Page for Market Testing
Description:
Design a modern Wix landing page for Veltoria+, an innovative concussion recovery and brain health supplement from a cutting-edge healthcare company. The page will focus on market testing, lead generation, and customer engagement with educational content.
________________________________________
1. Overview of Veltoria+
Business Name: Veltoria+
Industry: Health & Wellness / Nutraceutical Supplements
Project Goal:
Veltoria+ is a premium nutraceutical supplement designed to help prevent concussions and accelerate recovery from traumatic brain injuries (TBI). Every year, millions of people suffer concussions—whether from contact sports, military service, or accidents—which can lead to both short- and long-term cognitive, emotional, and physical impairments. Current treatment options are limited to rest and rehabilitation, with no QVX-approved medications to directly aid recovery.
Veltoria+ seeks to fill this gap by providing a science-backed, multi-ingredient formulation designed to reduce neuroinflammation, oxidative stress, and support mitochondrial function, helping the brain recover faster and more effectively. Our goal is to raise awareness of this innovative approach to concussion care, test market interest, and build an early community of customers and healthcare providers. This project will create a Wix-based landing page for market testing, lead generation, and educational outreach to gauge demand and prepare for future product launches.
2. Target Audience
Primary Audience:
1. Athletes:
o Individuals in high-contact sports (e.g., football, rugby, soccer) at risk for concussions, seeking supplements to help protect brain health and accelerate recovery.
2. Military Personnel and Veterans:
o Active-duty service members and veterans who are at higher risk of Traumatic Brain Injuries (TBI) and are interested in maintaining optimal cognitive function and recovery.
3. Older Adults:
o Individuals aged 60+ concerned about cognitive health and recovery after falls or injuries leading to concussions, looking for proactive brain health support.
4. Healthcare Professionals:
o Physicians, therapists, and other healthcare providers seeking cutting-edge, evidence-based supplements to recommend to patients dealing with concussions or TBI.
3. Landing Page Objectives
1. Market Testing:
The page’s primary goal is to gauge potential demand for Veltoria+ and collect valuable data through email sign-ups, lead generation forms, and user engagement.
2. Educational Content:
Provide high-level, non-proprietary information about concussions, brain health, and how Veltoria+ can support recovery. Emphasize the science-backed nature of the supplement without revealing the full ingredient formula. Position this content strategically to educate visitors before they convert.
3. Lead Capture:
Use compelling calls-to-action (CTAs) to encourage visitors to sign up for a waitlist, download an eBook on concussion recovery, or join an email list for updates. The primary goal is to gather emails and generate leads for future marketing efforts.
4. User Engagement and Blog:
Incorporate a blog section to provide visitors with more in-depth content about concussions, brain health, and recovery strategies. The blog should offer expert articles, recovery tips, and current scientific findings, helping to establish Veltoria+ as an authority on the subject. Ensure visitors are engaged with informative content, testimonials, and interactive elements like quizzes or polls that encourage participation and capture interest.
4. Key Design Requirements
4.1 General Style:
• Clean and Modern Design:
The landing page should have a professional, trustworthy feel while being modern and minimalistic. It should align with the health and wellness industry, using visuals and design elements that convey trust, support, and scientific credibility.
• Easy-to-Navigate Layout:
The page must be intuitive, with clearly defined sections that guide users effortlessly through the content, leading them to the CTA forms.
4.2 Specific Sections to Include:
1. Hero Section (Above the Fold):
o Headline: A compelling headline such as “Guard Your Mind. Bounce Back Sooner with Veltoria+.”
o Subtext: Briefly describe the supplement’s primary benefits, e.g., “Advanced nutraceutical formulation supporting brain health and faster concussion recovery.”
o Call to Action (CTA): Prominently feature a button like “Join the Waitlist” or “Download Free Recovery Guide.”
o Include a visually appealing background image or hero image that represents brain health or protection.
2. Benefits Section:
o Highlight key benefits in bullet points, such as:
Faster recovery from concussions – Veltoria+ accelerates recovery by reducing neuroinflammation and oxidative stress.
Protection against long-term brain damage – The supplement helps prevent lasting cognitive impairment from multiple or severe concussions.
Scientifically backed multi-pathway neuroprotection – Targets inflammation, oxidative damage, mitochondrial function, and synaptic health.
Improved cognitive function – Enhances mental clarity, focus, and energy post-concussion.
Preventive benefits for high-risk individuals – Athletes and those in high-risk professions can use Veltoria+ to proactively protect their brain.
Reduced symptoms post-injury – Helps alleviate symptoms like brain fog, headaches, dizziness, and fatigue.
Supports long-term brain health – Ingredients that promote neuroplasticity and overall cognitive well-being.
o Use simple, high-quality icons to visually represent each benefit.
3. Mechanism of Action Section:
o Explain how Veltoria+ works, focusing on the unique mechanisms of action without disclosing proprietary details. For example:
“Targets neuroinflammation, oxidative stress, and mitochondrial function to support brain recovery.”
Include infographics or simple diagrams showing how the supplement improves brain health by acting on multiple pathways.
4. Educational Section:
o This section, placed either below the hero section or above the FAQ section, will provide visitors with clear, digestible educational content about concussions. Topics may include:
What is a concussion?
Symptoms of concussions.
Long-term risks of untreated concussions.
The role of brain supplements in recovery.
Statistics and facts about concussions.
o This section is meant to establish Veltoria+ as a trusted authority on concussion care and brain health, driving credibility before visitors reach the CTA.
5. Educational Resources / Free Download:
o Offer a free eBook or concussion recovery guide as an incentive for visitors to provide their email. The guide should be high-quality and offer value (e.g., “The Ultimate Concussion Recovery Guide”).
o Include a lead capture form (integrated with Mailchimp or a similar tool) that collects name and email addresses in exchange for the guide.
6. Blog Section:
o Create a blog section with regularly updated articles focusing on topics like:
Concussion prevention and recovery tips.
The science behind concussion supplements.
Brain health maintenance for athletes and high-risk populations.
Interviews with healthcare experts or athletes discussing concussions.
o The blog should drive SEO and increase organic traffic to the website while positioning Veltoria+ as an expert in brain health.
7. Social Proof and Testimonials:
o Add sample or hypothetical testimonials from athletes, military personnel, or healthcare professionals who would use a product like Veltoria+.
o Incorporate high-quality images (e.g., stock photos or graphics) alongside these testimonials to increase credibility.
8. FAQ Section:
o A simple FAQ section answering common questions about the product, such as:
What is Veltoria+?
How does it help with concussion recovery?
Who can benefit from it?
Are there any side effects?
o This section should reassure visitors by addressing safety and benefits.
9. Compliance & Disclaimers:
o Include all necessary disclaimers (e.g., “These statements have not been evaluated by the QVX”) and certifications (e.g., “Manufactured in a GMP-Certified Facility”).
5. Functional Requirements
1. Platform:
The website must be built on Wix for ease of use, so we can make future edits or updates without technical expertise. It should leverage Wix’s SEO features and be integrated with Google Analytics for tracking.
2. Lead Capture Integration:
The site must include a lead capture form integrated with Mailchimp or another email marketing platform to collect user data. Ensure all data is stored securely and complies with GDPR regulations.
3. Mobile Responsiveness:
The landing page must be fully responsive across all devices (desktop, tablet, and mobile), ensuring a seamless experience for users.
4. SEO Best Practices:
Implement basic SEO techniques (e.g., meta titles, descriptions, keywords) to ensure that the page is optimized for search engines. Use heading tags appropriately to highlight key sections.
5. Fast Load Times:
Optimize the site for fast load times. Compress images and streamline any large media files to ensure visitors do not bounce due to slow page performance.
6. Additional Features to Consider
1. Interactive Elements (Optional):
Consider adding a quiz (e.g., “Are You at Risk for a Concussion?”) or a poll to engage users and collect more data on their interest and concerns.
o Quizzes can help personalize the user experience while allowing you to gather insights about your audience.
2. Exit-Intent Popup offering visitors a free guide or other incentives could help capture users just before they leave the page, increasing conversions. This feature could prompt users who were about to exit to sign up for updates or download the eBook.
3. A/B Testing Capabilities:
If possible, include A/B testing functionality on key elements like CTAs and form placements, so we can optimize the site’s conversion rate based on performance data.
7. Deliverables
1. Fully functional, mobile-responsive Wix website that meets the design and functional requirements outlined above.
2. Integration of lead capture form with Mailchimp or other marketing platforms.
3. Google Analytics setup for tracking user behavior, conversions, and traffic.
4. Source files for any custom graphics or visuals used on the site.
5. A handover guide or documentation on how we can make simple updates to the site using Wix.
Athletes, Military Personnel and Veterans, Healthcare Professionals, Older adults
1 page

```html
<!DOCTYPE html>
<html lang="en">
<head>
<meta charset="utf-8">
<title>Veltoria+ Landing Page</title>
<link href="https://fonts.googleapis.com/css2?family=Poppins:wght@300;400;500;600;700&display=swap" rel="stylesheet">
<style>
:root{
  --navy:#0c4a8a;
  --navy-deep:#0a3d78;
  --teal:#14a0a8;
  --teal-soft:#1fb3b8;
  --mint:#eefafb;
  --ice:#f1f6fd;
  --ink:#1d2b3a;
  --muted:#5b6773;
  --white:#ffffff;
  --star:#f5b400;
}
*{box-sizing:border-box;margin:0;padding:0}
html,body{width:1200px;height:2624px;overflow:hidden}
body{background:#eef1f5;font-family:'Poppins',sans-serif;color:var(--ink);position:relative}
.page{position:absolute;top:37px;width:537px;background:var(--white);box-shadow:0 4px 18px rgba(12,40,80,.12)}
.page--a{left:47px}
.page--b{left:621px;top:39px}
section,footer{position:relative;overflow:hidden}
.heading{position:absolute;left:0;right:0;text-align:center;font-size:20px;font-weight:400;color:var(--teal)}
.heading b{font-weight:700;color:var(--navy)}
.heading sup{font-size:12px;color:var(--navy);font-weight:600}
.btn{position:absolute;display:inline-block;font-size:6.5px;font-weight:600;color:var(--white);padding:5px 10px;border-radius:2px;white-space:nowrap}
.btn--navy{background:var(--navy)}
.btn--teal{background:var(--teal)}
.photo{display:block}

/* hero */
.hero{height:281px}
.hero--a .hero-bg{background:radial-gradient(circle at 70% 45%,#e0527a 0,#7a3bd0 14%,#1a6fb8 24%,#1d1d24 44%,#0c0c10 100%)}
.hero--b .hero-bg{background:linear-gradient(100deg,#2d6f68 0%,#4b8a78 45%,#c77a2a 72%,#f2a13a 82%,#6a3d1c 100%)}
.hero-bg{position:absolute;inset:0}
.nav{position:absolute;left:40px;top:0;width:457px;height:36px;background:var(--white);border-radius:0 0 8px 8px;display:flex;align-items:center;padding-left:96px;gap:0}
.nav-brand{position:absolute;left:0;top:0;width:72px;height:48px;background:var(--white);clip-path:polygon(0 0,100% 0,100% 78%,50% 100%,0 78%);display:flex;align-items:center;justify-content:center;gap:3px;font-size:7px;color:var(--navy);font-weight:600}
.brand-dot{width:7px;height:7px;border-radius:50%;background:var(--teal)}
.nav a{font-size:6.5px;color:var(--ink);text-decoration:none;margin-right:22px}
.nav a.active{color:var(--navy);font-weight:600;border-bottom:1px solid var(--navy)}
.nav .nav-cta{background:var(--teal);color:var(--white);padding:5px 7px;border-radius:2px;font-weight:600;margin-right:0}
.hero-title{position:absolute;left:48px;top:88px;font-size:17px;line-height:25px;color:var(--white);font-weight:300}
.hero-title b{font-weight:600}
.hero-sub{position:absolute;left:49px;top:168px;width:190px;font-size:6px;line-height:12px;color:#e4eaf0}
.hero .btn{top:200px}

/* how it works */
.how{height:297px;background:var(--mint)}
.how .heading{top:26px}
.step{position:absolute;width:210px;height:87px;background:var(--white);border-radius:6px;box-shadow:0 2px 8px rgba(12,74,138,.1);padding:16px 14px 0 24px}
.step h3{font-size:10px;font-weight:500;color:var(--navy);margin-bottom:8px}
.step p{font-size:5.6px;line-height:12px;color:var(--muted)}
.step-num{position:absolute;width:22px;height:22px;background:var(--navy);color:var(--white);font-size:7px;font-weight:600;display:flex;align-items:center;justify-content:center}
.step-icon{position:absolute;top:12px;right:16px;width:24px;height:20px}
.s1{left:49px;top:68px}.s1 .step-num{left:0;top:0;border-radius:6px 0 22px 0}
.s2{left:272px;top:68px;padding-left:14px}.s2 .step-num{right:0;top:0;border-radius:0 6px 0 22px}
.s3{left:49px;top:170px}.s3 .step-num{left:0;bottom:0;border-radius:0 22px 0 6px;background:var(--teal)}
.s4{left:272px;top:170px;padding-left:14px}.s4 .step-num{right:0;bottom:0;border-radius:22px 0 6px 0;background:var(--teal)}
.s2 .step-icon,.s4 .step-icon{right:26px}
.hub{position:absolute;left:244px;top:140px;width:50px;height:50px;border-radius:50%;background:var(--white);box-shadow:0 0 0 5px var(--mint);display:flex;align-items:center;justify-content:center}

/* benefits */
.benefits{height:272px}
.benefits .heading{top:26px}
.benefit{position:absolute;width:172px}
.benefit h4{font-size:6.5px;font-weight:500;color:var(--navy);margin-bottom:3px}
.benefit p{font-size:5.3px;line-height:9.5px;color:var(--muted)}
.benefit--l{left:42px;text-align:right}
.benefit--r{left:314px}
.b-icon{position:absolute;width:30px;height:30px;border-radius:50%}
.b-icon--l{left:222px;background:var(--navy)}
.b-icon--r{left:274px;background:var(--teal)}
.benefits .btn{top:222px}

/* educational guide */
.guide{height:300px;background:var(--mint)}
.guide .heading{top:26px}
.guide-card{position:absolute;top:70px;width:136px;height:152px;background:var(--white);border-radius:3px;box-shadow:0 2px 6px rgba(0,0,0,.08);padding:3px}
.guide-card .photo{height:120px;background:linear-gradient(135deg,#6b5448,#c79a80 55%,#3d3a3c)}
.guide-card p{font-size:6px;font-weight:500;text-align:center;margin-top:9px;line-height:9px}
.play{position:absolute;left:58px;top:51px;width:17px;height:17px;border-radius:50%;background:#e8221c}
.play::after{content:"";position:absolute;left:7px;top:5px;border-left:5px solid #fff;border-top:3.5px solid transparent;border-bottom:3.5px solid transparent}
.guide .btn{top:253px;left:243px}

/* resources */
.resources{height:311px}
.res-band{position:absolute;left:0;top:0;width:100%;height:211px;background:radial-gradient(circle at 50% 40%,#1d5ba3,#0b3e7e 70%)}
.resources .heading{top:30px;color:var(--white)}
.resources .heading b,.resources .heading sup{color:var(--white)}
.res-sub{position:absolute;top:64px;width:100%;text-align:center;font-size:8px;color:var(--white)}
.res-note{position:absolute;top:88px;width:100%;text-align:center;font-size:5.6px;color:#d7e4f4}
.form{position:absolute;left:81px;top:121px;width:376px;height:181px;background:var(--white);border-radius:3px;box-shadow:0 4px 12px rgba(0,0,0,.12);border-bottom:2px solid var(--navy)}
.field{position:absolute;height:17px;background:#e7f5f5;font-size:5.8px;padding:5px 6px;color:var(--ink)}
.field i{position:absolute;right:6px;top:5px;width:5px;height:5px;border-radius:50%;background:var(--navy)}
.form .btn{left:167px;top:140px}

/* blog */
.blog{height:365px}
.blog .heading{top:20px}
.post{position:absolute;top:61px;width:142px;height:218px;background:var(--white);box-shadow:0 2px 8px rgba(0,0,0,.1)}
.post .photo{height:84px}
.post-body{padding:8px 10px}
.post-date{font-size:5px;font-weight:600;color:var(--teal)}
.post h4{font-size:6.8px;font-weight:500;color:var(--navy);line-height:11px;margin:5px 0 5px}
.post p{font-size:5.3px;line-height:10.5px;color:var(--muted)}
.post .btn{position:static;margin-top:8px;font-size:4.8px;padding:4px 6px}
.post .play{left:62px;top:33px}
.blog .btn--more{top:318px;left:234px}

/* testimonials */
.testimonials{height:219px;background:var(--ice)}
.testimonials .heading{top:22px}
.quote{position:absolute;top:74px;width:170px;height:108px;background:var(--white);border-radius:6px;box-shadow:0 2px 8px rgba(0,0,0,.08);padding:10px 12px 0 38px}
.quote-mark{font-size:16px;font-weight:700;color:var(--navy);line-height:14px}
.quote p{font-size:5.8px;line-height:13.5px;color:var(--ink);margin-top:4px}
.quote-name{font-size:6px;font-weight:600;margin-top:2px}
.quote-name span{color:var(--star);letter-spacing:1px}
.avatar{position:absolute;width:53px;height:53px;border-radius:50%;border:3px solid var(--white)}
.arrow{position:absolute;top:123px;width:12px;height:12px;border-radius:50%;background:var(--teal)}

/* faq */
.faq{height:260px}
.faq .heading{top:22px}
.faq-item{position:absolute;left:49px;width:213px;height:18px;border-radius:9px;background:#e9f0f6;font-size:6px;font-weight:500;color:var(--ink);padding:5px 12px}
.faq-item.open{background:var(--teal);color:var(--white)}
.faq-item i{position:absolute;right:6px;top:5px;width:8px;height:8px;border-radius:50%;border:1px solid currentColor}
.faq-text{position:absolute;left:282px;width:200px;font-size:5.3px;line-height:12px;color:var(--muted)}
.faq .btn{top:212px;left:243px}

/* footer */
.footer{height:242px;background:var(--teal);color:var(--white)}
.foot-brand{position:absolute;left:48px;top:60px;display:flex;align-items:center;gap:5px;font-size:11px;font-weight:500}
.foot-brand .brand-dot{width:11px;height:11px;background:var(--white)}
.foot-col{position:absolute;top:32px}
.foot-col h5{font-size:8px;font-weight:500;margin-bottom:8px}
.foot-col li{list-style:none;font-size:6px;line-height:15.5px}
.foot-col li::before{content:"→ ";font-size:6px}
.contact li::before{content:"";display:inline-block;width:9px;height:9px;border-radius:50%;background:var(--white);margin-right:6px;vertical-align:middle}
.copyright{position:absolute;top:157px;width:100%;text-align:center;font-size:6.2px}
.disclaimer{position:absolute;top:187px;left:60px;width:350px;text-align:center;font-size:6px;line-height:15px}
.seal{position:absolute;left:408px;top:170px;width:48px;height:48px;border-radius:50%;background:radial-gradient(circle,#d9b34a 0 45%,#2b2b2b 47% 100%)}
</style>
</head>
<body>

<main class="page page--a">
  <section class="hero hero--a">
    <div class="hero-bg" role="img" aria-label="Colourful brain bursting with paint splashes on a dark background"></div>
    <nav class="nav">
      <div class="nav-brand"><span class="brand-dot"></span>Veltoria+</div>
      <a class="active">Home</a><a>Benefits</a><a>Educational</a><a>Mechanism</a><a>Blog</a><a>FAQ</a><a class="nav-cta">Contact Us</a>
    </nav>
    <h1 class="hero-title">Guard Your<br><b>Mind. Bounce Back Sooner</b><br>with <b>Veltoria</b>+</h1>
    <p class="hero-sub">Advanced nutraceutical formulation supporting brain health and faster concussion recovery.</p>
    <span class="btn btn--navy" style="left:49px">Join the Waitlist</span>
    <span class="btn btn--teal" style="left:124px">Download Free Recovery Guide</span>
  </section>

  <section class="how">
    <h2 class="heading"><b>How Its</b> Work<sup>+</sup></h2>
    <div class="step s1"><span class="step-num">01</span><svg class="step-icon" viewBox="0 0 24 20"><path d="M2 8h20v10H2z" fill="#0c4a8a"/><path d="M2 11q3-3 5 0t5 0 5 0 5 0" stroke="#fff" fill="none"/><circle cx="6" cy="4" r="1.5" fill="#0c4a8a"/><circle cx="12" cy="3" r="1.5" fill="#0c4a8a"/><circle cx="18" cy="4" r="1.5" fill="#0c4a8a"/></svg><h3>Neuroinflammation</h3><p>Reducing inflammation can help protect neurons and promote healing. This can be achieved through lifestyle changes, diet, and certain supplements.</p></div>
    <div class="step s2"><span class="step-num">02</span><svg class="step-icon" viewBox="0 0 24 20"><g stroke="#0c4a8a" stroke-width="1.5"><path d="M6 5l6 5 6-6M12 10l-3 7"/></g><circle cx="6" cy="5" r="3" fill="#0c4a8a"/><circle cx="18" cy="4" r="3" fill="#14a0a8"/><circle cx="12" cy="10" r="2.5" fill="#0c4a8a"/><circle cx="9" cy="17" r="2.5" fill="#0c4a8a"/></svg><h3>Oxidative Stress</h3><p>Antioxidants can help neutralize free radicals, reducing oxidative damage. Nutrients like vitamins C and E, and compounds like glutathione, are often beneficial.</p></div>
    <div class="step s3"><span class="step-num">03</span><svg class="step-icon" viewBox="0 0 24 20"><rect x="7" y="1" width="10" height="18" rx="5" fill="#14a0a8"/><path d="M9 6q3 2 6 0M9 10q3 2 6 0M9 14q3 2 6 0" stroke="#fff" fill="none"/></svg><h3>Mitochondrial Function</h3><p>Supporting mitochondrial health can improve energy production in brain cells. Nutrients like coenzyme Q10 and omega-3 fatty acids may enhance mitochondrial function.</p></div>
    <div class="step s4"><span class="step-num">04</span><svg class="step-icon" viewBox="0 0 24 20"><circle cx="12" cy="9" r="8" fill="#14a0a8"/><path d="M8 9h8M12 5v8" stroke="#fff"/></svg><h3>Support brain recovery</h3><p>Supporting mitochondrial health can improve energy production in brain cells. Nutrients like coenzyme Q10 and omega-3 fatty acids may enhance mitochondrial function.</p></div>
    <div class="hub"><span class="brand-dot" style="width:18px;height:18px;background:var(--navy)"></span></div>
  </section>

  <section class="benefits">
    <h2 class="heading"><b>Our</b> Benefits<sup>+</sup></h2>
    <div class="benefit benefit--l" style="top:68px"><h4>Faster recovery from concussions</h4><p>Veltoria+ accelerates recovery by reducing neuroinflammation and oxidative stress.</p></div>
    <div class="benefit benefit--r" style="top:68px"><h4>Improved cognitive function</h4><p>Athletes and those in high-risk professions can use Veltoria+ to proactively protect their brain.</p></div>
    <div class="benefit benefit--l" style="top:117px"><h4>Protection against long-term brain damage</h4><p>The supplement helps prevent lasting cognitive impairment from multiple or severe concussions.</p></div>
    <div class="benefit benefit--r" style="top:117px"><h4>Reduced symptoms post-injury</h4><p>Helps alleviate symptoms like brain fog, headaches, dizziness, and fatigue.</p></div>
    <div class="benefit benefit--l" style="top:166px"><h4>Multi-pathway neuroprotection</h4><p>– Targets inflammation, oxidative damage, mitochondrial function, and synaptic health.</p></div>
    <div class="benefit benefit--r" style="top:166px"><h4>Supports long-term brain health</h4><p>Ingredients that promote neuroplasticity and overall cognitive well-being.</p></div>
    <span class="b-icon b-icon--l" style="top:69px"></span><span class="b-icon b-icon--r" style="top:69px"></span>
    <span class="b-icon b-icon--l" style="top:118px;background:var(--teal)"></span><span class="b-icon b-icon--r" style="top:118px;background:var(--navy)"></span>
    <span class="b-icon b-icon--l" style="top:167px"></span><span class="b-icon b-icon--r" style="top:167px"></span>
    <span class="btn btn--navy" style="left:206px">View More</span>
    <span class="btn btn--teal" style="left:273px">Get Started</span>
  </section>

  <section class="guide">
    <h2 class="heading"><b>Our</b> Educational Guide<sup>+</sup></h2>
    <div class="guide-card" style="left:49px"><div class="photo" role="img" aria-label="Injured athlete lying on the field being checked by a medic"></div><p>What is a concussion?</p></div>
    <div class="guide-card" style="left:201px"><div class="photo" role="img" aria-label="Man holding his head in pain, video thumbnail"></div><span class="play"></span><p>Symptoms of concussions</p></div>
    <div class="guide-card" style="left:353px"><div class="photo" role="img" aria-label="Young woman holding her forehead with a headache"></div><p>Long-term risks of untreated concussions</p></div>
    <span class="btn btn--navy">View More</span>
  </section>

  <section class="resources">
    <div class="res-band" role="img" aria-label="Deep blue band with a faint brain texture"></div>
    <h2 class="heading"><b>Our Educational</b> Resources<sup>+</sup></h2>
    <p class="res-sub">The Ultimate Concussion Recovery Guide</p>
    <p class="res-note">Offer a free eBook or concussion recovery guide</p>
    <div class="form">
      <div class="field" style="left:14px;top:17px;width:171px">Name<i></i></div>
      <div class="field" style="left:191px;top:17px;width:171px">Email<i></i></div>
      <div class="field" style="left:14px;top:40px;width:171px">Phone Number<i></i></div>
      <div class="field" style="left:191px;top:40px;width:171px">Address<i></i></div>
      <div class="field" style="left:14px;top:63px;width:348px;height:60px">Message<i></i></div>
      <span class="btn btn--navy">Submit</span>
    </div>
  </section>

  <section class="blog">
    <h2 class="heading"><b>Our</b> Blog<sup>+</sup></h2>
    <article class="post" style="left:49px"><div class="photo" role="img" aria-label="Helmeted football player with glowing brain overlay" style="background:linear-gradient(135deg,#1b2a33,#c2562c 50%,#23333c)"></div><span class="play"></span><div class="post-body"><div class="post-date">14TH OCTOBER 2024</div><h4>Concussion prevention &amp; recovery tips.</h4><p>Practical steps to lower risk, spot warning signs early and rest well after a knock.</p><span class="btn btn--navy">LEARN MORE</span></div></article>
    <article class="post" style="left:197px"><div class="photo" role="img" aria-label="Brain model beside supplement capsules in a lab" style="background:linear-gradient(135deg,#7fa8c9,#e8dcc4 50%,#3d6a8e)"></div><span class="play"></span><div class="post-body"><div class="post-date">14TH OCTOBER 2024</div><h4>The science behind concussion supplements.</h4><p>How key nutrients act on inflammation, oxidation and cell energy after an injury.</p><span class="btn btn--navy">LEARN MORE</span></div></article>
    <article class="post" style="left:345px"><div class="photo" role="img" aria-label="Athlete training with a balance ball in a gym" style="background:linear-gradient(135deg,#4a4e54,#9aa0a6 50%,#2f3236)"></div><span class="play"></span><div class="post-body"><div class="post-date">14TH OCTOBER 2024</div><h4>Brain health maintenance for athletes &amp; high-risk populations.</h4><p>Daily habits that help active people keep their minds sharp over time.</p><span class="btn btn--navy">LEARN MORE</span></div></article>
    <span class="btn btn--navy btn--more">View More Blog</span>
  </section>

  <section class="testimonials">
    <h2 class="heading"><b>What Our</b> Customer Says<sup>+</sup></h2>
    <span class="arrow" style="left:19px"></span><span class="arrow" style="left:507px"></span>
    <div class="quote" style="left:87px"><div class="quote-mark">“</div><p>Recovery felt steadier and my focus came back sooner than I expected after my fall.</p><div class="quote-name">Mara <span>★★★★★</span></div></div>
    <div class="avatar" role="img" aria-label="Portrait of an older customer" style="left:59px;top:101px;background:linear-gradient(135deg,#c9c2ba,#8a7f75)"></div>
    <div class="quote" style="left:306px"><div class="quote-mark">“</div><p>As a swimmer I train hard, and this routine helps me feel clear and ready each day.</p><div class="quote-name">Delan <span>★★★★★</span></div></div>
    <div class="avatar" role="img" aria-label="Swimmer in a pool" style="left:278px;top:101px;background:linear-gradient(135deg,#1c8fb4,#0b4f72)"></div>
  </section>

  <section class="faq">
    <h2 class="heading"><b>Frequently</b> Asked Questions<sup>+</sup></h2>
    <div class="faq-item open" style="top:80px">What is Veltoria+?<i></i></div>
    <div class="faq-item" style="top:108px">Who can benefit from it?<i></i></div>
    <div class="faq-item" style="top:136px">How does it help with concussion recovery?<i></i></div>
    <div class="faq-item" style="top:164px">Who can benefit from it?<i></i></div>
    <p class="faq-text" style="top:78px">Veltoria+ is a daily nutraceutical blend built to support the brain after a concussion. It targets inflammation, oxidative stress and cell energy so the recovery process can move along with less strain on the body.</p>
    <p class="faq-text" style="top:140px">Athletes, service members, older adults and care providers looking for science-backed brain support can all use it as part of a wider recovery plan guided by a doctor.</p>
    <span class="btn btn--navy">View More</span>
  </section>

  <footer class="footer">
    <div class="foot-brand"><span class="brand-dot"></span>Veltoria+</div>
    <div class="foot-col" style="left:194px"><h5>Quick Links</h5><ul><li>Home</li><li>About</li><li>Educational</li><li>Mechanism</li><li>Contact Us</li></ul></div>
    <div class="foot-col" style="left:292px"><h5>Help Links</h5><ul><li>FAQ</li><li>Terms of use</li><li>Privacy Policy</li><li>Support Links</li><li>Conditions</li></ul></div>
    <div class="foot-col contact" style="left:385px"><h5>Contact Us</h5><ul><li>Veltoria+, Harbor City</li><li>+1 555 010 4422</li><li>hello@veltoria.com</li></ul></div>
    <p class="copyright">Copyrights@2024. Veltoria+. All Rights Reserved</p>
    <p class="disclaimer">Disclaimers - These statements have not been evaluated by the QVX and certifications. Manufactured in a GMP- Certified Facility.</p>
    <span class="seal" role="img" aria-label="Certification seal"></span>
  </footer>
</main>

<main class="page page--b">
  <section class="hero hero--b">
    <div class="hero-bg" role="img" aria-label="Side profile of a head with a glowing orange brain on a teal background"></div>
    <nav class="nav">
      <div class="nav-brand"><span class="brand-dot"></span>Veltoria+</div>
      <a class="active">Home</a><a>Benefits</a><a>Educational</a><a>Mechanism</a><a>Blog</a><a>FAQ</a><a class="nav-cta">Contact Us</a>
    </nav>
    <h1 class="hero-title">Guard Your<br><b>Mind. Bounce Back Sooner</b><br>with <b>Veltoria</b>+</h1>
    <p class="hero-sub">Advanced nutraceutical formulation supporting brain health and faster concussion recovery.</p>
    <span class="btn btn--navy" style="left:49px">Join the Waitlist</span>
    <span class="btn btn--teal" style="left:124px">Download Free Recovery Guide</span>
  </section>

  <section class="how">
    <h2 class="heading"><b>How Its</b> Work<sup>+</sup></h2>
    <div class="step s1"><span class="step-num">01</span><svg class="step-icon" viewBox="0 0 24 20"><path d="M2 8h20v10H2z" fill="#0c4a8a"/><path d="M2 11q3-3 5 0t5 0 5 0 5 0" stroke="#fff" fill="none"/><circle cx="6" cy="4" r="1.5" fill="#0c4a8a"/><circle cx="12" cy="3" r="1.5" fill="#0c4a8a"/><circle cx="18" cy="4" r="1.5" fill="#0c4a8a"/></svg><h3>Neuroinflammation</h3><p>Reducing inflammation can help protect neurons and promote healing. This can be achieved through lifestyle changes, diet, and certain supplements.</p></div>
    <div class="step s2"><span class="step-num">02</span><svg class="step-icon" viewBox="0 0 24 20"><g stroke="#0c4a8a" stroke-width="1.5"><path d="M6 5l6 5 6-6M12 10l-3 7"/></g><circle cx="6" cy="5" r="3" fill="#0c4a8a"/><circle cx="18" cy="4" r="3" fill="#14a0a8"/><circle cx="12" cy="10" r="2.5" fill="#0c4a8a"/><circle cx="9" cy="17" r="2.5" fill="#0c4a8a"/></svg><h3>Oxidative Stress</h3><p>Antioxidants can help neutralize free radicals, reducing oxidative damage. Nutrients like vitamins C and E, and compounds like glutathione, are often beneficial.</p></div>
    <div class="step s3"><span class="step-num">03</span><svg class="step-icon" viewBox="0 0 24 20"><rect x="7" y="1" width="10" height="18" rx="5" fill="#14a0a8"/><path d="M9 6q3 2 6 0M9 10q3 2 6 0M9 14q3 2 6 0" stroke="#fff" fill="none"/></svg><h3>Mitochondrial Function</h3><p>Supporting mitochondrial health can improve energy production in brain cells. Nutrients like coenzyme Q10 and omega-3 fatty acids may enhance mitochondrial function.</p></div>
    <div class="step s4"><span class="step-num">04</span><svg class="step-icon" viewBox="0 0 24 20"><circle cx="12" cy="9" r="8" fill="#14a0a8"/><path d="M8 9h8M12 5v8" stroke="#fff"/></svg><h3>Support brain recovery</h3><p>Supporting mitochondrial health can improve energy production in brain cells. Nutrients like coenzyme Q10 and omega-3 fatty acids may enhance mitochondrial function.</p></div>
    <div class="hub"><span class="brand-dot" style="width:18px;height:18px;background:var(--navy)"></span></div>
  </section>

  <section class="benefits">
    <h2 class="heading"><b>Our</b> Benefits<sup>+</sup></h2>
    <div class="benefit benefit--l" style="top:68px"><h4>Faster recovery from concussions</h4><p>Veltoria+ accelerates recovery by reducing neuroinflammation and oxidative stress.</p></div>
    <div class="benefit benefit--r" style="top:68px"><h4>Improved cognitive function</h4><p>Athletes and those in high-risk professions can use Veltoria+ to proactively protect their brain.</p></div>
    <div class="benefit benefit--l" style="top:117px"><h4>Protection against long-term brain damage</h4><p>The supplement helps prevent lasting cognitive impairment from multiple or severe concussions.</p></div>
    <div class="benefit benefit--r" style="top:117px"><h4>Reduced symptoms post-injury</h4><p>Helps alleviate symptoms like brain fog, headaches, dizziness, and fatigue.</p></div>
    <div class="benefit benefit--l" style="top:166px"><h4>Multi-pathway neuroprotection</h4><p>– Targets inflammation, oxidative damage, mitochondrial function, and synaptic health.</p></div>
    <div class="benefit benefit--r" style="top:166px"><h4>Supports long-term brain health</h4><p>Ingredients that promote neuroplasticity and overall cognitive well-being.</p></div>
    <span class="b-icon b-icon--l" style="top:69px"></span><span class="b-icon b-icon--r" style="top:69px"></span>
    <span class="b-icon b-icon--l" style="top:118px;background:var(--teal)"></span><span class="b-icon b-icon--r" style="top:118px;background:var(--navy)"></span>
    <span class="b-icon b-icon--l" style="top:167px"></span><span class="b-icon b-icon--r" style="top:167px"></span>
    <span class="btn btn--navy" style="left:206px">View More</span>
    <span class="btn btn--teal" style="left:273px">Get Started</span>
  </section>

  <section class="guide">
    <h2 class="heading"><b>Our</b> Educational Guide<sup>+</sup></h2>
    <div class="guide-card" style="left:49px"><div class="photo" role="img" aria-label="Injured athlete lying on the field being checked by a medic"></div><p>What is a concussion?</p></div>
    <div class="guide-card" style="left:201px"><div class="photo" role="img" aria-label="Man holding his head in pain, video thumbnail"></div><span class="play"></span><p>Symptoms of concussions</p></div>
    <div class="guide-card" style="left:353px"><div class="photo" role="img" aria-label="Young woman holding her forehead with a headache"></div><p>Long-term risks of untreated concussions</p></div>
    <span class="btn btn--navy">View More</span>
  </section>

  <section class="resources">
    <div class="res-band" role="img" aria-label="Deep blue band with a faint brain texture"></div>
    <h2 class="heading"><b>Our Educational</b> Resources<sup>+</sup></h2>
    <p class="res-sub">The Ultimate Concussion Recovery Guide</p>
    <p class="res-note">Offer a free eBook or concussion recovery guide</p>
    <div class="form">
      <div class="field" style="left:14px;top:17px;width:171px">Name<i></i></div>
      <div class="field" style="left:191px;top:17px;width:171px">Email<i></i></div>
      <div class="field" style="left:14px;top:40px;width:171px">Phone Number<i></i></div>
      <div class="field" style="left:191px;top:40px;width:171px">Address<i></i></div>
      <div class="field" style="left:14px;top:63px;width:348px;height:60px">Message<i></i></div>
      <span class="btn btn--navy">Submit</span>
    </div>
  </section>

  <section class="blog">
    <h2 class="heading"><b>Our</b> Blog<sup>+</sup></h2>
    <article class="post" style="left:49px"><div class="photo" role="img" aria-label="Helmeted football player with glowing brain overlay" style="background:linear-gradient(135deg,#1b2a33,#c2562c 50%,#23333c)"></div><span class="play"></span><div class="post-body"><div class="post-date">14TH OCTOBER 2024</div><h4>Concussion prevention &amp; recovery tips.</h4><p>Practical steps to lower risk, spot warning signs early and rest well after a knock.</p><span class="btn btn--navy">LEARN MORE</span></div></article>
    <article class="post" style="left:197px"><div class="photo" role="img" aria-label="Brain model beside supplement capsules in a lab" style="background:linear-gradient(135deg,#7fa8c9,#e8dcc4 50%,#3d6a8e)"></div><span class="play"></span><div class="post-body"><div class="post-date">14TH OCTOBER 2024</div><h4>The science behind concussion supplements.</h4><p>How key nutrients act on inflammation, oxidation and cell energy after an injury.</p><span class="btn btn--navy">LEARN MORE</span></div></article>
    <article class="post" style="left:345px"><div class="photo" role="img" aria-label="Athlete training with a balance ball in a gym" style="background:linear-gradient(135deg,#4a4e54,#9aa0a6 50%,#2f3236)"></div><span class="play"></span><div class="post-body"><div class="post-date">14TH OCTOBER 2024</div><h4>Brain health maintenance for athletes &amp; high-risk populations.</h4><p>Daily habits that help active people keep their minds sharp over time.</p><span class="btn btn--navy">LEARN MORE</span></div></article>
    <span class="btn btn--navy btn--more">View More Blog</span>
  </section>

  <section class="testimonials">
    <h2 class="heading"><b>What Our</b> Customer Says<sup>+</sup></h2>
    <span class="arrow" style="left:19px"></span><span class="arrow" style="left:507px"></span>
    <div class="quote" style="left:87px"><div class="quote-mark">“</div><p>Recovery felt steadier and my focus came back sooner than I expected after my fall.</p><div class="quote-name">Mara <span>★★★★★</span></div></div>
    <div class="avatar" role="img" aria-label="Portrait of an older customer" style="left:59px;top:101px;background:linear-gradient(135deg,#c9c2ba,#8a7f75)"></div>
    <div class="quote" style="left:306px"><div class="quote-mark">“</div><p>As a swimmer I train hard, and this routine helps me feel clear and ready each day.</p><div class="quote-name">Delan <span>★★★★★</span></div></div>
    <div class="avatar" role="img" aria-label="Swimmer in a pool" style="left:278px;top:101px;background:linear-gradient(135deg,#1c8fb4,#0b4f72)"></div>
  </section>

  <section class="faq">
    <h2 class="heading"><b>Frequently</b> Asked Questions<sup>+</sup></h2>
    <div class="faq-item open" style="top:80px">What is Veltoria+?<i></i></div>
    <div class="faq-item" style="top:108px">Who can benefit from it?<i></i></div>
    <div class="faq-item" style="top:136px">How does it help with concussion recovery?<i></i></div>
    <div class="faq-item" style="top:164px">Who can benefit from it?<i></i></div>
    <p class="faq-text" style="top:78px">Veltoria+ is a daily nutraceutical blend built to support the brain after a concussion. It targets inflammation, oxidative stress and cell energy so the recovery process can move along with less strain on the body.</p>
    <p class="faq-text" style="top:140px">Athletes, service members, older adults and care providers looking for science-backed brain support can all use it as part of a wider recovery plan guided by a doctor.</p>
    <span class="btn btn--navy">View More</span>
  </section>

  <footer class="footer">
    <div class="foot-brand"><span class="brand-dot"></span>Veltoria+</div>
    <div class="foot-col" style="left:194px"><h5>Quick Links</h5><ul><li>Home</li><li>About</li><li>Educational</li><li>Mechanism</li><li>Contact Us</li></ul></div>
    <div class="foot-col" style="left:292px"><h5>Help Links</h5><ul><li>FAQ</li><li>Terms of use</li><li>Privacy Policy</li><li>Support Links</li><li>Conditions</li></ul></div>
    <div class="foot-col contact" style="left:385px"><h5>Contact Us</h5><ul><li>Veltoria+, Harbor City</li><li>+1 555 010 4422</li><li>hello@veltoria.com</li></ul></div>
    <p class="copyright">Copyrights@2024. Veltoria+. All Rights Reserved</p>
    <p class="disclaimer">Disclaimers - These statements have not been evaluated by the QVX and certifications. Manufactured in a GMP- Certified Facility.</p>
    <span class="seal" role="img" aria-label="Certification seal"></span>
  </footer>
</main>

</body>
</html>
```